GLUMV Powerpoint Template

A powerpoint template for our new brand of private label components which are built for us in Asia. We are looking for a fresh design for our powerpoint template. Note the subtle overlay of the fox in our theme. We like this as it implies quickness. Do not overuse the fox theme. It needs to be very subtle if used.

Our products include High performance passive RF and Fiber components and cable solutions for the wireless industry. Our comprehensive product portfolios include both general and low PIM grades and are widely used for cellular towers and in-building DAS systems as well as in the wireless research and development labs.

Common models include:
Filters
Diplexers, triplexers and 5plexers
Splitters and combiners
Signal tappers
Couplers
Terminations load and attenuators
Jumper cables and testing cables assemblies
Fiber Splice Trays
Patch Panels
Fiber Jumpers & Adapters

```html
<!DOCTYPE html>
<html lang="en">
<head>
<meta charset="utf-8">
<title>GLUMV Presentation Slide</title>
<link href="https://fonts.googleapis.com/css2?family=Khand:wght@500;600&family=Exo+2:wght@400&display=swap" rel="stylesheet">
<style>
  :root {
    --brand-red: #e5161d;
    --slide-bg: #f8f8f8;
    --panel-white: #ffffff;
    --ink-dark: #444444;
    --ink-body: #4a4a4a;
    --tab-black: #0d0d0d;
    --footer-red: #e40f17;
    --footer-red-deep: #d00c13;
    --footer-red-soft: #ec2a30;
    --white: #ffffff;
  }
  * { margin: 0; padding: 0; box-sizing: border-box; }
  html, body {
    width: 1200px;
    height: 900px;
    overflow: hidden;
    background: var(--slide-bg);
  }
  .slide {
    position: relative;
    width: 1200px;
    height: 900px;
    background: var(--slide-bg);
    overflow: hidden;
  }
  .slide-title {
    position: absolute;
    left: 31px;
    top: 20px;
    font-family: "Khand", sans-serif;
    font-weight: 600;
    font-size: 60px;
    line-height: 1;
    color: var(--brand-red);
    letter-spacing: 0.6px;
  }
  .brand-name {
    position: absolute;
    right: 64px;
    top: 34px;
    font-family: "Khand", sans-serif;
    font-weight: 600;
    font-size: 78px;
    line-height: 1;
    color: var(--brand-red);
    letter-spacing: 10px;
  }
  .page-tab {
    position: absolute;
    right: 0;
    top: 0;
    width: 50px;
    height: 93px;
    background: var(--tab-black);
    display: flex;
    align-items: center;
    justify-content: center;
  }
  .page-tab-label {
    transform: rotate(-90deg);
    font-family: "Khand", sans-serif;
    font-weight: 600;
    font-size: 22px;
    color: var(--white);
    white-space: nowrap;
    letter-spacing: 0.5px;
  }
  .content-heading {
    position: absolute;
    left: 30px;
    top: 155px;
    font-family: "Khand", sans-serif;
    font-weight: 600;
    font-size: 38px;
    line-height: 1;
    color: var(--ink-dark);
  }
  .content-body {
    position: absolute;
    left: 31px;
    top: 210px;
    width: 636px;
    font-family: "Exo 2", sans-serif;
    font-weight: 400;
    font-size: 22.5px;
    line-height: 36px;
    color: var(--ink-body);
  }
  .content-body p + p { margin-top: 36px; }
  .text-line {
    display: block;
    white-space: nowrap;
    text-align: justify;
    text-align-last: justify;
  }
  .text-line.is-last {
    text-align: left;
    text-align-last: left;
  }
  .image-slot {
    position: absolute;
    left: 720px;
    top: 210px;
    width: 438px;
    height: 487px;
    background: var(--panel-white);
    border-radius: 4px;
    display: flex;
    align-items: center;
    justify-content: center;
  }
  .image-slot-label {
    font-family: Arial, Helvetica, sans-serif;
    font-size: 24px;
    color: var(--brand-red);
  }
  .footer-band {
    position: absolute;
    left: 0;
    bottom: 0;
    width: 1200px;
    height: 56px;
    background:
      radial-gradient(ellipse 300px 40px at 20% 40%, var(--footer-red-soft) 0%, transparent 100%),
      radial-gradient(ellipse 320px 40px at 70% 60%, var(--footer-red-soft) 0%, transparent 100%),
      linear-gradient(180deg, var(--footer-red) 0%, var(--footer-red-deep) 100%);
    display: flex;
    align-items: center;
    padding-left: 11px;
  }
  .footer-copyright {
    font-family: "Khand", sans-serif;
    font-weight: 500;
    font-size: 20px;
    color: var(--white);
  }
</style>
</head>
<body>
<main class="slide">
  <h1 class="slide-title">PROJECT TITLE HERE</h1>
  <div class="brand-name">GLUMV</div>
  <div class="page-tab"><span class="page-tab-label">PAGE-1</span></div>

  <h2 class="content-heading">Lorem ipsum dolor sit ipsum</h2>
  <div class="content-body">
    <p>
      <span class="text-line">Lorem ipsum dolor sit ipsum Lorem ipsum dolor sit</span>
      <span class="text-line">ipsum Lorem ipsum dolor sit ipsum Lorem ipsum dolor</span>
      <span class="text-line">sit ipsum lorem ipsum dolor sit ipsum Lorem ipsum</span>
      <span class="text-line is-last">dolor sit ipsum Lorem ipsum dolor sit ipsum</span>
    </p>
    <p>
      <span class="text-line">Lorem ipsum dolor sit ipsum Lorem ipsum dolor sit</span>
      <span class="text-line">ipsum Lorem ipsum dolor sit ipsum Lorem ipsum dolor</span>
      <span class="text-line">sit ipsum lorem ipsum dolor sit ipsum Lorem ipsum</span>
      <span class="text-line">dolor sit ipsum Lorem ipsum dolor sit ipsum Lorem</span>
      <span class="text-line is-last">ipsum dolor sit ipsum</span>
    </p>
    <p>
      <span class="text-line">Lorem ipsum dolor sit ipsum Lorem ipsum dolor sit</span>
      <span class="text-line">ipsum Lorem ipsum dolor sit ipsum Lorem ipsum dolor</span>
      <span class="text-line">sit ipsum lorem ipsum dolor sit ipsum Lorem ipsum</span>
    </p>
  </div>

  <div class="image-slot"><span class="image-slot-label">IMG HERE</span></div>

  <footer class="footer-band" role="img" aria-label="Red footer band with a subtle hexagon texture">
    <span class="footer-copyright">Copyright text ghere</span>
  </footer>
</main>
</body>
</html>
```